Corvant Systems Business Card

Create an appealing and elegant Business card for corvant systems. Include logo and use related colors from website, be creative. Include Business name, my name, tile, address, contacts, address, and social media contacts if possible. Logo PSD file is attached.

Bleed Area: 3.46" x 2.32"
Trim: 3.3" x 2.16"
Safe Area: 3.14" x 2.02"

Save files as vector-based PDF with outlined text and PNG.
No crop marks
CMYK color setting

Business Card Info:

Corvant Systems

Dennis Halvorsen
Owner

512 Brindlemoor Rd Unit C
Harlow Bend, MR 02871
t. 1.888.555.0162
e. dennis.h@corvantsys.example
w. www.corvantsys.example

facebook. www.linkcircle.example/CorvantSys
twitter. chirpline.example/corvantsys
pinterest. www.pinterest.com/corvantsys/

Target Market(s)

Business Owners and Partners

Industry/Entity Type

Business

Requirements
Must have
• Logo and related colors from website

```html
<!DOCTYPE html>
<html lang="en">
<head>
<meta charset="utf-8">
<title>Corvant Systems Business Card</title>
<link rel="stylesheet" href="https://fonts.googleapis.com/css2?family=Saira:wght@300;400;500;600&display=swap">
<style>
  :root {
    --backdrop: #2b2b2b;
    --card: #f7f7f8;
    --ink: #1c1c1c;
    --muted: #555a61;
    --brand-blue: #4a6fa8;
    --brand-black: #0d0d0d;
    --rule: #c9ccd1;
    --on-blue: #ffffff;
  }
  * { box-sizing: border-box; margin: 0; padding: 0; }
  html, body {
    width: 1200px; height: 800px; overflow: hidden;
    background: var(--backdrop);
    font-family: "Saira", sans-serif;
    color: var(--ink);
  }
  .stage {
    position: relative; width: 1200px; height: 800px;
    display: flex; align-items: center; justify-content: center; gap: 50px;
  }
  .card {
    position: relative; width: 540px; height: 354px;
    background: var(--card); overflow: hidden;
    border-radius: 4px;
  }

  /* Contact side */
  .wordmark {
    font-family: "Saira", sans-serif; font-weight: 600;
    color: var(--ink); letter-spacing: 0.5px; line-height: 1;
  }
  .contact-side .wordmark {
    position: absolute; left: 30px; top: 34px; font-size: 30px;
  }
  .identity {
    position: absolute; right: 34px; top: 132px; text-align: right;
  }
  .identity .person { font-size: 21px; font-weight: 400; color: var(--ink); }
  .identity .divider { color: var(--brand-blue); margin: 0 6px; }
  .identity .role { font-size: 16px; color: var(--muted); font-weight: 300; }
  .identity .company { font-size: 18px; font-weight: 400; }
  .identity .company .accent { color: var(--brand-blue); }
  .top-rule {
    position: absolute; left: 0; right: 34px; top: 210px;
    height: 1px; background: var(--rule);
  }
  .details {
    position: absolute; right: 34px; top: 220px; width: 430px;
    font-size: 13px; font-weight: 400; color: var(--ink); line-height: 1.7;
  }
  .details .row { display: flex; justify-content: space-between; }
  .details .address { text-align: right; }
  .contact-band { position: absolute; left: 0; bottom: 0; width: 540px; height: 64px; }
  .band-url {
    position: absolute; left: 30px; bottom: 22px;
    font-size: 13px; color: var(--brand-blue); letter-spacing: 0.3px;
  }

  /* Brand side */
  .brand-side .wordmark {
    position: absolute; left: 0; right: 0; top: 108px;
    text-align: center; font-size: 54px;
  }
  .social-band {
    position: absolute; left: 0; right: 0; top: 238px; height: 72px;
    background: var(--brand-blue);
    border-top: 2px solid var(--rule); border-bottom: 2px solid var(--rule);
    color: var(--on-blue); font-size: 13px;
  }
  .social { position: absolute; display: flex; align-items: center; gap: 8px; }
  .social .dot { width: 14px; height: 14px; border-radius: 50%; background: var(--on-blue); }
  .social.primary { left: 28px; top: 12px; }
  .social.secondary { left: 274px; top: 12px; }
  .social.tertiary { right: 28px; top: 42px; }
</style>
</head>
<body>
<main class="stage">

  <section class="card contact-side" aria-label="Business card, contact side">
    <div class="wordmark">Corvant Systems</div>

    <div class="identity">
      <p class="person">Dennis Halvorsen<span class="divider">|</span><span class="role">owner</span></p>
      <p class="company"><span class="accent">Corvant</span> Systems</p>
    </div>

    <div class="top-rule"></div>

    <div class="details">
      <div class="row"><span>1.888.555.0162</span><span>dennis.h@corvantsys.example</span></div>
      <p class="address">512 Brindlemoor Rd Unit C, Harlow Bend, MR 02871</p>
    </div>

    <svg class="contact-band" viewBox="0 0 540 64" aria-hidden="true">
      <rect x="0" y="0" width="540" height="64" fill="var(--brand-black)"/>
      <polygon points="300,14 540,14 540,64 272,64" fill="var(--brand-blue)"/>
      <rect x="300" y="12" width="240" height="1.5" fill="var(--rule)"/>
    </svg>
    <p class="band-url">www.corvantsys.example</p>
  </section>

  <section class="card brand-side" aria-label="Business card, brand side">
    <div class="wordmark">Corvant Systems</div>

    <div class="social-band">
      <div class="social primary"><span class="dot"></span>www.linkcircle.example/CorvantSys</div>
      <div class="social secondary"><span class="dot"></span>chirpline.example/corvantsys</div>
      <div class="social tertiary"><span class="dot"></span>www.pinwall.example/corvantsys</div>
    </div>
  </section>

</main>
</body>
</html>
```